App Screenshots

We need professional looking screenshots for out apps Thought Arena and Thought Arena Plus.
The screenshots should incorporate text highlighting features or other significant details.
You can see the current screenshots here:
https://apps.examplestore.test/details?id=cortexo.thoughtarena
And here is some of our competition.
Neuro Duel:
https://apps.examplestore.test/details?id=jp.co.kavemori.neuroduel
Quorvex
https://apps.examplestore.test/details?id=com.quorvexhub.quorvex
Some example to use in the screenshots:
Thought Arena "exercise your brain"
Used by over 8 million people
Nearly three dozen brain training games to challenge you daily
Discover your strengths and weaknesses
Exercise a broad range of cognitive skills
Based on principles of cognitive psychology
For the pro version, text can also be added:
The training center selects games for you based on your strengths and weaknesses
The text doesn't have to be exactly the same if you can think of something better, or need to modify it to fit.
We need the ability to modify the text and insert different screenshots into the images. This will allow us to modify them for multiple languages. PSD files preferred. Raw screenshots are attached for convenience.

```html
<!DOCTYPE html>
<html lang="en">
<head>
<meta charset="utf-8">
<title>Thought Arena – Games</title>
<link rel="stylesheet" href="https://fonts.googleapis.com/css2?family=Roboto+Slab:wght@700&family=Roboto:wght@300;400;500&display=swap">
<style>
:root{
  --sky-top:#1c7fd6;
  --sky-bottom:#12c3fb;
  --white:#ffffff;
  --device-grey:#9a9a9a;
  --bar-blue:#0d4c9c;
  --list-bg:#e4e4e4;
  --band-grey:#8a8a8a;
  --progress-track:#d8d8d8;
  --progress-fill:#ffc400;
  --score-blue:#0d4c9c;
  --ink:#111111;
  --nav-black:#0a0a0a;
  --memory-purple:#5b1a5e;
  --learning-pink:#ff1f55;
  --anticipation-red:#ff0000;
  --attention-cyan:#1fb4f0;
}
*{box-sizing:border-box;margin:0;padding:0}
html,body{width:674px;height:1200px;overflow:hidden}
body{background:var(--sky-top)}
.stage{position:absolute;left:0;top:0;width:680px;height:1210px;transform:scale(.99118,.99174);transform-origin:0 0;
  background:linear-gradient(170deg,var(--sky-top) 0%,var(--sky-bottom) 100%);overflow:hidden;font-family:'Roboto',sans-serif}
.headline{position:absolute;top:48px;width:100%;text-align:center;font-family:'Roboto Slab',serif;font-weight:700;font-size:37px;color:var(--white)}
.tagline{position:absolute;top:136px;width:100%;text-align:center;font-weight:300;font-size:34px;line-height:42px;color:var(--white);white-space:nowrap}
.device{position:absolute;left:100px;top:330px;width:482px;height:900px;background:var(--white);border-radius:60px 60px 0 0/28px 28px 0 0}
.device-key{position:absolute;background:var(--white);border-radius:3px}
.key-left{left:92px;top:517px;width:10px;height:152px}
.key-right{left:580px;top:452px;width:10px;height:66px}
.lens{position:absolute;border-radius:50%;background:var(--device-grey)}
.lens-small{left:169px;top:371px;width:13px;height:13px}
.lens-large{left:328px;top:363px;width:24px;height:24px}
.screen{position:absolute;left:115px;top:411px;width:448px;height:800px;background:var(--list-bg);overflow:hidden}
.status-bar{height:36px;background:var(--bar-blue);display:flex;justify-content:flex-end;align-items:center;gap:6px;padding-right:8px;color:var(--white);font-size:18px}
.app-bar{height:55px;background:var(--bar-blue);position:relative;color:var(--white)}
.app-bar h1{text-align:center;font-weight:500;font-size:24px;line-height:55px}
.app-bar svg{position:absolute;left:12px;top:15px}
.game-card{position:absolute;left:9px;width:429px;height:177px;background:var(--white);border-radius:16px;overflow:hidden}
.game-icon{position:absolute;left:13px;top:12px;width:118px;height:118px;border-radius:50%}
.game-title{position:absolute;left:140px;right:6px;top:22px;text-align:center;font-size:20px;color:var(--ink);white-space:nowrap}
.game-title.small{font-size:14px;top:28px}
.progress{position:absolute;left:167px;top:61px;width:226px;height:12px;border-radius:6px;background:var(--progress-track)}
.progress span{display:block;height:100%;border-radius:6px;background:var(--progress-fill)}
.best{position:absolute;left:140px;right:6px;top:96px;text-align:center;font-size:20px;color:var(--score-blue)}
.category{position:absolute;left:0;bottom:0;width:100%;height:35px;background:var(--band-grey);color:var(--white);text-align:center;font-weight:300;font-size:20px;line-height:35px}
.nav-bar{position:absolute;left:0;top:739px;width:100%;height:61px;background:var(--nav-black);display:flex;justify-content:space-around;align-items:center;padding:0 60px}
.zoom-lens{position:absolute;left:405px;top:500px;width:198px;height:198px;border-radius:50%;background:var(--white);border:5px solid #e9eef3;box-shadow:0 2px 8px rgba(0,0,0,.25);overflow:hidden}
.zoom-title{position:absolute;left:-34px;top:18px;font-size:33px;white-space:nowrap;color:var(--ink)}
.zoom-bar{position:absolute;left:4px;top:82px;width:185px;height:18px;border-radius:9px;background:var(--progress-fill)}
.zoom-best{position:absolute;left:22px;top:133px;font-size:31px;font-weight:500;color:var(--score-blue)}
.feature-badge{position:absolute;left:60px;top:862px;width:202px;height:202px;border-radius:50%;background:rgba(255,255,255,.5);display:flex;align-items:center;justify-content:center}
.feature-badge .disc{width:180px;height:180px;border-radius:50%;background:var(--anticipation-red);border:4px solid var(--white)}
</style>
</head>
<body>
<main class="stage">
  <h2 class="headline">Lorem Ipsum</h2>
  <p class="tagline">Nearly three dozen brain training games<br>to challenge you daily</p>

  <div class="device-key key-left"></div>
  <div class="device-key key-right"></div>
  <div class="device"></div>
  <div class="lens lens-small"></div>
  <div class="lens lens-large"></div>

  <section class="screen">
    <div class="status-bar">
      <svg width="44" height="20" viewBox="0 0 44 20"><path d="M2 7a14 14 0 0 1 20 0l-10 12z" fill="#fff"/><path d="M26 19h14V3z" fill="#fff"/></svg>
      <svg width="12" height="20" viewBox="0 0 12 20"><rect x="4" y="0" width="4" height="2" fill="#fff"/><rect x="1" y="2" width="10" height="18" rx="1" fill="#fff"/></svg>
      <span>12:06</span>
    </div>
    <header class="app-bar">
      <svg width="32" height="26" viewBox="0 0 32 26"><path d="M30 13H4M14 2 3 13l11 11" stroke="#fff" stroke-width="3.5" fill="none"/></svg>
      <h1>Games</h1>
    </header>

    <article class="game-card" style="top:105px">
      <div class="game-icon" style="background:var(--memory-purple)" role="img" aria-label="Memory match game icon with four letter tiles"></div>
      <div class="game-title">MEMORY MATCH</div>
      <div class="progress"><span style="width:75%"></span></div>
      <div class="best">Best: 75%</div>
      <div class="category">Learning Strategy</div>
    </article>

    <article class="game-card" style="top:297px">
      <div class="game-icon" style="background:var(--learning-pink)" role="img" aria-label="Object learning game icon with a camera-like object"></div>
      <div class="game-title small">SELF-ORDERED LEARNING FOR OBJECTS</div>
      <div class="progress"><span style="width:80%"></span></div>
      <div class="best">Best: 80%</div>
      <div class="category">Learning Strategy</div>
    </article>

    <article class="game-card" style="top:490px">
      <div class="game-title">ANTICIPATION</div>
      <div class="progress"><span style="width:86%"></span></div>
      <div class="best">Best: 85%</div>
      <div class="category">Divided Attention</div>
    </article>

    <article class="game-card" style="top:683px">
      <div class="game-icon" style="background:var(--attention-cyan)" role="img" aria-label="Divided attention game icon"></div>
      <div class="game-title">DIVIDED ATTENTION Level 1</div>
    </article>

    <nav class="nav-bar">
      <svg width="44" height="26" viewBox="0 0 44 26"><path d="M10 4 3 11l7 7M3 11h30a8 8 0 0 1 0 14H14" stroke="#aaa" stroke-width="2.5" fill="none"/></svg>
      <svg width="48" height="26" viewBox="0 0 48 26"><path d="M3 24V12L24 3l21 9v12z" stroke="#aaa" stroke-width="2.5" fill="none"/></svg>
      <svg width="44" height="26" viewBox="0 0 44 26"><rect x="3" y="9" width="34" height="15" stroke="#aaa" stroke-width="2.5" fill="none"/><path d="M8 5h33v14" stroke="#aaa" stroke-width="2.5" fill="none"/></svg>
    </nav>
  </section>

  <div class="zoom-lens">
    <div class="zoom-title">MEMORY MATCH</div>
    <div class="zoom-bar"></div>
    <div class="zoom-best">Best: 75%</div>
  </div>

  <div class="feature-badge">
    <div class="disc" role="img" aria-label="Anticipation game icon, enlarged"></div>
  </div>
</main>
</body>
</html>
```